Triathlon coaching company website design

A website is needed for a coaching company called StrideVantage. The company provides coaching services to triathletes and other endurance athletes. This includes 1:1 coaching, individualized training plan development, race preparation, and access to guidance and advice on all aspects of developing and maintaining a healthy lifestyle. The design should appeal to all levels of athletes, but be professional in appearance. The tone of the site should be in keeping with the company tagline: Endurance. Resilience. Achievement.

Target Market(s)

All levels of triathletes - beginners to professionals

Industry/Entity Type

It Company

Coding

Coded - Design and coding required

Number of Pages Required

1 page

Colors

Designer to choose colors to be used in the design.

Requirements
Must have
• Pages that should be included must cover: Introductory (Home), description in detail of what we do, description of the main coach (bio) and others types of expert advisors who can be available, link to contact the company, race reports for coaches and athletes that can be regularly updated, links to other sites of potential interest (e.g. other triathlon sites or my facebook page), twitter feed, sign up for email updates. Ability to add other links and pages in future months (e.g. shared calendar access to book meetings, credit card functionality, testimonials)
Should not have
• Not loud or down market feel - target market will largely be highly educated and reasonably affluent

```html
<!DOCTYPE html>
<html lang="en">
<head>
<meta charset="utf-8">
<title>StrideVantage — Triathlon Coaching</title>
<link href="https://fonts.googleapis.com/css2?family=Montserrat:wght@400;500;600;700&family=Open+Sans:wght@400;600&display=swap" rel="stylesheet">
<style>
:root{
  --red:#b3201f;
  --red-dark:#8e1716;
  --ink:#222;
  --muted:#666;
  --dark:#1b1b1b;
  --footer:#121212;
  --bar:#0b0b0b;
  --white:#fff;
}
*{margin:0;padding:0;box-sizing:border-box}
html,body{width:1200px;height:2900px;overflow:hidden}
body{position:relative;font-family:"Open Sans",Arial,sans-serif;color:var(--ink);background:#fff}
h1,h2,h3,h4,.nav,.btn{font-family:"Montserrat",Arial,sans-serif}

/* header + hero */
.hero{position:absolute;top:0;left:0;width:1200px;height:520px;
  background:linear-gradient(180deg,#2a3440 0%,#4d6472 45%,#7c93a0 70%,#3a4a55 100%)}
.site-header{position:absolute;top:0;left:0;width:1200px;height:80px;display:flex;align-items:center;justify-content:space-between;padding:0 60px}
.brand{font-family:"Montserrat",sans-serif;font-weight:700;font-size:30px;color:var(--red)}
.nav{display:flex;gap:34px;align-items:center;font-size:15px;font-weight:500;color:#fff}
.nav .cta{background:var(--red);padding:8px 14px}
.hero-copy{position:absolute;top:170px;left:110px;color:#fff}
.hero-copy h1{font-size:58px;font-weight:500;letter-spacing:1px}
.btn{display:inline-block;background:var(--red);color:#fff;font-weight:500;font-size:17px;padding:16px 30px;border-radius:3px}
.hero-copy .btn{margin-top:26px}
.hero-dots{position:absolute;right:26px;top:290px;display:flex;flex-direction:column;gap:12px}
.hero-dots span{width:14px;height:14px;border-radius:50%;background:rgba(255,255,255,.55)}
.hero-dots span:first-child{background:#fff}

/* services */
.services{position:absolute;top:500px;left:88px;width:1024px;height:550px;background:var(--red)}
.services h2{text-align:center;color:#fff;font-weight:500;font-size:54px;margin-top:28px}
.service-cards{position:absolute;top:120px;left:28px;display:flex;gap:22px}
.service-card{position:relative;width:308px;height:320px;overflow:hidden}
.service-card .photo{position:absolute;inset:0}
.service-card .overlay{position:absolute;inset:0;padding:150px 22px 0;text-align:center;color:#fff;background:linear-gradient(180deg,rgba(179,32,31,0) 0%,rgba(179,32,31,.55) 45%,rgba(140,20,20,.9) 100%)}
.service-card h3{font-size:18px;font-weight:600;text-transform:uppercase;margin-bottom:8px}
.service-card p{font-size:13px;line-height:1.45}
.service-card .more{display:inline-block;margin-top:12px;background:var(--red-dark);font-family:"Montserrat",sans-serif;font-size:12px;padding:7px 14px;border:1px solid rgba(255,255,255,.4)}
.slider-dots{position:absolute;bottom:38px;left:0;width:100%;display:flex;justify-content:center;gap:12px}
.slider-dots span{width:13px;height:13px;border-radius:50%;background:#1f1f1f}
.slider-dots span.on{background:#fff}

/* about */
.about{position:absolute;top:1130px;left:88px;width:1024px;height:380px}
.about .media{position:absolute;left:0;top:10px;width:490px;height:340px;background:linear-gradient(135deg,#9aa2aa,#5f6a74 60%,#2e3740)}
.play{position:absolute;left:205px;top:130px}
.about .text{position:absolute;left:520px;top:0;width:504px}
.about h2{color:var(--red);font-size:54px;font-weight:600}
.about .rule{width:60px;height:3px;background:var(--red);margin:8px 0 16px}
.about p{font-size:12.5px;line-height:1.6;color:var(--muted);margin-bottom:12px}
.about .btn{font-size:14px;padding:11px 20px;margin-top:6px}

/* testimonial */
.testimonial{position:absolute;top:1550px;left:0;width:1200px;height:370px;background:linear-gradient(90deg,#1a1a1a,#2c2c2c 50%,#1a1a1a);color:#fff}
.testimonial h2{text-align:center;font-size:34px;font-weight:500;margin-top:36px}
.avatar{position:absolute;left:150px;top:135px;width:126px;height:126px;border-radius:50%;background:linear-gradient(135deg,#c9b3a3,#7d6a60);border:4px solid #fff}
.quote{position:absolute;left:310px;top:140px;width:800px;font-size:16px;line-height:1.75}
.author{position:absolute;left:310px;top:290px;font-size:17px;font-weight:600}
.arrow{position:absolute;top:170px}
.arrow.left{left:22px}.arrow.right{right:22px}

/* articles */
.articles{position:absolute;top:1960px;left:88px;width:1024px}
.articles h2{text-align:center;color:var(--red);font-size:46px;font-weight:700;margin-top:20px}
.article-grid{display:flex;gap:17px;margin-top:32px}
.article{position:relative;width:330px;height:320px;overflow:hidden}
.article .info{position:absolute;left:0;bottom:0;width:100%;padding:18px 18px 20px;color:#fff;background:linear-gradient(180deg,rgba(0,0,0,0),rgba(0,0,0,.75))}
.article .date{display:flex;align-items:center;gap:7px;font-size:12px;margin-bottom:6px}
.article h4{font-size:15px;font-weight:600;line-height:1.35}

/* footer */
.site-footer{position:absolute;top:2440px;left:0;width:1200px;height:390px;background:var(--footer);color:#ddd}
.site-footer h4{font-size:17px;font-weight:500;color:#fff;letter-spacing:.5px;margin-bottom:22px}
.col{position:absolute;top:70px}
.col.contact{left:88px;width:360px}
.col.mail{left:540px;width:330px}
.col.links{left:960px;width:160px}
.row{display:flex;gap:14px;align-items:flex-start;font-size:14px;line-height:1.5;margin-bottom:16px}
.row .name{color:#fff;font-weight:600;font-size:15px}
.mail p{font-size:14px;line-height:1.5;margin-bottom:16px}
.field{width:300px;height:40px;background:#fff;margin-bottom:12px;font-size:13px;color:#888;padding:11px 12px}
.mail .btn{font-size:14px;padding:11px 22px}
.links ul{list-style:none;font-size:14px;line-height:2}
.links li::before{content:"› ";color:var(--red)}
.bottom-bar{position:absolute;top:2830px;left:0;width:1200px;height:70px;background:var(--bar);color:#bbb;font-size:13px;display:flex;align-items:center;justify-content:space-between;padding:0 88px}
.social{display:flex;gap:10px;align-items:center}
.social span{width:26px;height:26px;border-radius:50%;background:#666}
.social span:nth-child(2){background:#2b5aa6}.social span:nth-child(3){background:#2a95d8}
.social span:nth-child(4){background:var(--red)}.social span:nth-child(5){background:#c7442c}
</style>
</head>
<body>

<section class="hero" role="img" aria-label="Swimmer in goggles and cap mid-stroke in a pool"></section>
<header class="site-header">
  <div class="brand">StrideVantage</div>
  <nav class="nav">
    <span>HOME</span><span>WHAT WE DO</span><span>BIO</span><span>RACE REPORTS</span><span class="cta">CONTACT US</span>
  </nav>
</header>
<div class="hero-copy">
  <h1>Endurance. Resilience. Achievement.</h1>
  <span class="btn">Get Started</span>
</div>
<div class="hero-dots"><span></span><span></span><span></span></div>

<section class="services">
  <h2>StrideVantage Services</h2>
  <div class="service-cards">
    <article class="service-card">
      <div class="photo" role="img" aria-label="Group of runners training together" style="background:linear-gradient(135deg,#8a8f95,#4d5258)"></div>
      <div class="overlay">
        <h3>1:1 Coaching</h3>
        <p>Personal sessions that focus on your goals, your pace and the steady build of every discipline.</p>
        <span class="more">Read more ›</span>
      </div>
    </article>
    <article class="service-card">
      <div class="photo" role="img" aria-label="Coach reviewing a plan with an athlete" style="background:linear-gradient(135deg,#9c9a96,#5a5550)"></div>
      <div class="overlay">
        <h3>Consultation</h3>
        <p>Talk through your season with an expert and leave with a clear plan for race preparation.</p>
        <span class="more">Read more ›</span>
      </div>
    </article>
    <article class="service-card">
      <div class="photo" role="img" aria-label="Athlete working out in a gym" style="background:linear-gradient(135deg,#a09488,#5c5048)"></div>
      <div class="overlay">
        <h3>Lifestyle Coaching</h3>
        <p>Guidance on nutrition, rest and healthy habits that keep you strong beyond race day.</p>
        <span class="more">Read more ›</span>
      </div>
    </article>
  </div>
  <div class="slider-dots"><span></span><span class="on"></span><span></span></div>
</section>

<section class="about">
  <div class="media" role="img" aria-label="Head coach standing in a team jacket, video still">
    <svg class="play" width="80" height="80" viewBox="0 0 80 80" aria-hidden="true"><circle cx="40" cy="40" r="38" fill="#b3201f"/><path d="M32 25 L57 40 L32 55 Z" fill="#fff"/></svg>
  </div>
  <div class="text">
    <h2>About me</h2>
    <div class="rule"></div>
    <p>Triathlon is my passion. Over the years I have raced every distance and coached athletes of all levels, from first timers to seasoned competitors. I understand the demands of balancing training with work, family and a busy life, and I build plans that respect that balance while still pushing toward real progress. Every athlete is different, and coaching should be too.</p>
    <p>My own path began with a single sprint race and grew into long course events around the world. Along the way I learned how patience, consistency and honest feedback shape lasting results. Today I work alongside a small group of expert advisors in nutrition, strength and recovery so that every athlete has support in each part of their preparation.</p>
    <span class="btn">READ MORE ›</span>
  </div>
</section>

<section class="testimonial">
  <h2>WHAT PEOPLE SAY ABOUT US</h2>
  <svg class="arrow left" width="20" height="34" viewBox="0 0 20 34" aria-hidden="true"><path d="M17 3 L4 17 L17 31" fill="none" stroke="#fff" stroke-width="3"/></svg>
  <div class="avatar" role="img" aria-label="Portrait of a satisfied athlete"></div>
  <p class="quote">Lorem Ipsum is simply dummy text of the printing and typesetting industry. Lorem Ipsum has been the industry's standard dummy text ever since the 1500s, when an unknown printer took a galley of type and scrambled it to make a type specimen book. It has survived not only five centuries, but also the leap into electronic typesetting.</p>
  <div class="author">- Marion T. Hale</div>
  <svg class="arrow right" width="20" height="34" viewBox="0 0 20 34" aria-hidden="true"><path d="M3 3 L16 17 L3 31" fill="none" stroke="#fff" stroke-width="3"/></svg>
</section>

<section class="articles">
  <h2>LATEST ARTICLES</h2>
  <div class="article-grid">
    <article class="article" role="img" aria-label="Cyclist racing on a road" style="background:linear-gradient(160deg,#6f6a66,#3b3633)">
      <div class="info">
        <div class="date"><svg width="13" height="13" viewBox="0 0 13 13" aria-hidden="true"><rect x="1" y="2" width="11" height="10" fill="none" stroke="#fff"/><line x1="1" y1="5" x2="12" y2="5" stroke="#fff"/></svg>Jun 12, 2018</div>
        <h4>Section 1.10.32 of "de Finibus Bonorum" written by Varenus in 45 BC.</h4>
      </div>
    </article>
    <article class="article" role="img" aria-label="Crowd of runners at a race start" style="background:linear-gradient(160deg,#8b6f6a,#463632)">
      <div class="info">
        <div class="date"><svg width="13" height="13" viewBox="0 0 13 13" aria-hidden="true"><rect x="1" y="2" width="11" height="10" fill="none" stroke="#fff"/><line x1="1" y1="5" x2="12" y2="5" stroke="#fff"/></svg>Jun 12, 2018</div>
        <h4>Section 1.10.32 of "de Finibus Bonorum" written by Varenus in 45 BC.</h4>
      </div>
    </article>
    <article class="article" role="img" aria-label="Athlete resting after a workout" style="background:linear-gradient(160deg,#7d8288,#3d4146)">
      <div class="info">
        <div class="date"><svg width="13" height="13" viewBox="0 0 13 13" aria-hidden="true"><rect x="1" y="2" width="11" height="10" fill="none" stroke="#fff"/><line x1="1" y1="5" x2="12" y2="5" stroke="#fff"/></svg>Jun 12, 2018</div>
        <h4>Section 1.10.32 of "de Finibus Bonorum" written by Varenus in 45 BC.</h4>
      </div>
    </article>
  </div>
</section>

<footer class="site-footer">
  <div class="col contact">
    <h4>CONTACT US</h4>
    <div class="row">
      <svg width="16" height="20" viewBox="0 0 16 20" aria-hidden="true"><path d="M8 1a6 6 0 0 0-6 6c0 5 6 12 6 12s6-7 6-12a6 6 0 0 0-6-6z" fill="#b3201f"/><circle cx="8" cy="7" r="2.2" fill="#121212"/></svg>
      <div><div class="name">StrideVantage</div>4120 Harbor Ridge Road,<br>Elm Vale, 60482</div>
    </div>
    <div class="row">
      <svg width="16" height="16" viewBox="0 0 16 16" aria-hidden="true"><path d="M3 1l3 3-2 2c1 2 3 4 5 5l2-2 3 3-2 3C7 15 1 9 1 3z" fill="#b3201f"/></svg>
      <div>Phone : 0198 765 432</div>
    </div>
    <div class="row">
      <svg width="16" height="14" viewBox="0 0 16 14" aria-hidden="true"><rect x="1" y="2" width="14" height="10" fill="none" stroke="#b3201f" stroke-width="1.6"/><path d="M1 2l7 6 7-6" fill="none" stroke="#b3201f" stroke-width="1.6"/></svg>
      <div>Email : info@stridevantage.com</div>
    </div>
  </div>
  <div class="col mail">
    <h4>JOIN THE MAILING LIST</h4>
    <p>Stay informed about the<br>latest and greatest here at StrideVantage</p>
    <div class="field">Name</div>
    <div class="field">Email Address</div>
    <span class="btn">SUBSCRIBE</span>
  </div>
  <div class="col links">
    <h4>QUICK LINKS</h4>
    <ul><li>Home</li><li>What We Do</li><li>Bio</li><li>Race Reports</li><li>Contact Us</li></ul>
  </div>
</footer>
<div class="bottom-bar">
  <span>Copyright © 2018, StrideVantage. All rights reserved.</span>
  <div class="social">Follow us:<span></span><span></span><span></span><span></span><span></span></div>
</div>

</body>
</html>
```